New Plumbing Company

We are looking for a smart and creative business card design for our new plumbing company. We are looking for creativity and originality in our business cards.

Industry/Entity Type

Plumbing

Contact Information for Business Card

Crestline Plumbing
Peter Halvane
Managing Director
Telephone Number : 0481529604
Email : service@crestlineplumbing.com.au
Website : www.crestlineplumbing.com.au
Lic. 508264K

Colors
0692cd
33a6d7
000000

Requirements
Must have
• I want the business card to be designed on a black background using the blue tones i have selected as seen in the company logo.

```html
<!DOCTYPE html>
<html lang="en">
<head>
<meta charset="utf-8">
<title>Crestline Plumbing – Business Card</title>
<link href="https://fonts.googleapis.com/css2?family=Jost:wght@400;500&display=swap" rel="stylesheet">
<style>
  :root {
    --backdrop: #2e2927;
    --card-black: #1d1919;
    --brand-blue: #0692cd;
    --light-blue: #33a6d7;
    --stripe-grey: #9a9a9a;
    --text-white: #f2f2f2;
    --text-soft: #cfcfcf;
    --ghost: rgba(255,255,255,0.06);
  }
  * { box-sizing: border-box; margin: 0; padding: 0; }
  html, body {
    width: 1200px; height: 768px; overflow: hidden;
    background: var(--backdrop);
    font-family: "Jost", "Futura", sans-serif;
  }
  .stage {
    width: 1200px; height: 768px;
    display: flex; align-items: center; justify-content: center; gap: 60px;
  }
  .card {
    position: relative;
    width: 500px; height: 286px;
    background: var(--card-black);
    overflow: hidden;
    box-shadow: 0 10px 30px rgba(0,0,0,0.45);
  }

  /* brand name lockup */
  .brand {
    display: flex; align-items: center; gap: 14px;
    color: var(--brand-blue);
    font-weight: 400;
  }
  .brand-dot {
    flex: none;
    border: 3px solid var(--brand-blue);
    border-radius: 50%;
  }
  .brand-name { line-height: 1; letter-spacing: 0.5px; }

  /* front */
  .card-front { display: flex; align-items: center; justify-content: center; }
  .card-front .brand-dot { width: 46px; height: 46px; }
  .card-front .brand-name { font-size: 34px; }

  /* back */
  .stripe-blue {
    position: absolute; left: 0; top: 0; bottom: 0; width: 34px;
    background: var(--brand-blue);
  }
  .stripe-grey {
    position: absolute; left: 34px; top: 0; bottom: 0; width: 7px;
    background: var(--stripe-grey);
  }
  .card-back .brand { position: absolute; left: 80px; top: 40px; }
  .card-back .brand-dot { width: 38px; height: 38px; }
  .card-back .brand-name { font-size: 28px; }

  .person { position: absolute; left: 80px; top: 118px; }
  .person-name { color: var(--brand-blue); font-size: 21px; font-weight: 400; }
  .person-title { color: var(--text-soft); font-size: 11.5px; margin-top: 2px; }

  .licence {
    position: absolute; right: 28px; top: 122px;
    font-size: 14px; color: var(--text-white); letter-spacing: 0.5px;
  }
  .licence-label { color: var(--brand-blue); }

  .contacts { position: absolute; left: 80px; top: 178px; list-style: none; }
  .contacts li {
    display: flex; align-items: center; gap: 10px;
    color: var(--text-white); font-size: 13.5px; line-height: 22px;
  }
  .contacts svg { width: 12px; height: 12px; flex: none; fill: var(--text-soft); }

  .ghost-circle {
    position: absolute; right: -30px; bottom: -50px;
    width: 200px; height: 200px; border-radius: 50%;
    border: 6px solid var(--ghost);
  }
</style>
</head>
<body>
<main class="stage">
  <section class="card card-front" aria-label="Business card front">
    <div class="brand">
      <span class="brand-dot"></span>
      <span class="brand-name">Crestline Plumbing</span>
    </div>
  </section>

  <section class="card card-back" aria-label="Business card back">
    <div class="stripe-blue"></div>
    <div class="stripe-grey"></div>
    <div class="ghost-circle"></div>

    <div class="brand">
      <span class="brand-dot"></span>
      <span class="brand-name">Crestline Plumbing</span>
    </div>

    <div class="person">
      <p class="person-name">Peter Halvane</p>
      <p class="person-title">Managing Director</p>
    </div>

    <p class="licence"><span class="licence-label">LIC.</span> 508264K</p>

    <ul class="contacts">
      <li>
        <svg viewBox="0 0 24 24" aria-hidden="true"><path d="M6.6 10.8a15.1 15.1 0 0 0 6.6 6.6l2.2-2.2a1 1 0 0 1 1-.25 11.4 11.4 0 0 0 3.6.57 1 1 0 0 1 1 1V20a1 1 0 0 1-1 1A17 17 0 0 1 3 4a1 1 0 0 1 1-1h3.5a1 1 0 0 1 1 1c0 1.25.2 2.45.57 3.57a1 1 0 0 1-.25 1z"/></svg>
        0481529604
      </li>
      <li>
        <svg viewBox="0 0 24 24" aria-hidden="true"><path d="M12 2a10 10 0 1 0 0 20 10 10 0 0 0 0-20zm6.9 6h-2.9a15.6 15.6 0 0 0-1.4-3.6A8 8 0 0 1 18.9 8zM12 4c.8 1.2 1.5 2.5 1.9 4h-3.8c.4-1.5 1.1-2.8 1.9-4zM4.3 14a8 8 0 0 1 0-4h3.4a16 16 0 0 0 0 4zm.8 2h2.9c.3 1.3.8 2.5 1.4 3.6A8 8 0 0 1 5.1 16zM8 8H5.1a8 8 0 0 1 4.3-3.6C8.8 5.5 8.3 6.7 8 8zm4 12c-.8-1.2-1.5-2.5-1.9-4h3.8c-.4 1.5-1.1 2.8-1.9 4zm2.3-6H9.7a14.7 14.7 0 0 1 0-4h4.6a14.7 14.7 0 0 1 0 4zm.3 5.6c.6-1.1 1.1-2.3 1.4-3.6h2.9a8 8 0 0 1-4.3 3.6zm1.7-5.6a16 16 0 0 0 0-4h3.4a8 8 0 0 1 0 4z"/></svg>
        www.crestlineplumbing.com.au
      </li>
      <li>
        <svg viewBox="0 0 24 24" aria-hidden="true"><path d="M2 5h20v14H2zm2 2v.5l8 5 8-5V7zm0 2.8V17h16V9.8l-8 5z"/></svg>
        service@crestlineplumbing.com.au
      </li>
    </ul>
  </section>
</main>
</body>
</html>
```